Acupuncture business needs business card design

I need a business card for an acupuncture clinic called "Summit Wellpath"
It will need the following details:
My name: Marcus Thelwick
Acupuncturist
Member KPTG
BVF Treatment Provider
Ph numbers: 482 1358 027 514 3820
Email: marcus@swpath.example.nz
On the back it will need a table with 2 columns for appointments, one column for time and one for date.

Industry/Entity Type

Clinic

Contact Information for Business Card

Marcus Thelwick
Acupuncturist
Member KPTG
BVF Treatment Provider
Email: marcus@swpath.example.nz

Requirements
Must have
• Marcus Thelwick
• Acupuncturist
• Member KPTG
• BVF Treatment Provider
• Ph numbers: 482 1358 027 514 3820
• Email: marcus@swpath.example.nz
• On the back it will need a table with 2 columns for appointments, one column for time and one for date.

```html
<!DOCTYPE html>
<html lang="en">
<head>
<meta charset="utf-8">
<title>Summit Wellpath – Double-Sided Business Card</title>
<link rel="stylesheet" href="https://fonts.googleapis.com/css2?family=Barlow+Semi+Condensed:wght@600&family=Source+Sans+3:wght@400;500&family=Questrial&display=swap">
<style>
  :root {
    --sheet: #ffffff;
    --ink: #111111;
    --rule: #9a9a9a;
    --card-edge: #b5b5b5;
    --brand-blue: #1aa6df;
    --teal: #167d92;
    --table-line: #2a8ea6;
    --on-teal: #ffffff;
  }
  * { box-sizing: border-box; margin: 0; padding: 0; }
  html, body { width: 1200px; height: 848px; overflow: hidden; background: var(--sheet); }
  .sheet { position: relative; width: 1200px; height: 848px; }

  .sheet-title {
    position: absolute; left: 244px; top: 138px;
    font: 600 13px/1 "Barlow Semi Condensed", sans-serif; color: var(--ink); letter-spacing: .2px;
  }
  .sheet-rule { position: absolute; left: 244px; top: 154px; width: 714px; height: 1px; background: var(--rule); }
  .sheet-size {
    position: absolute; left: 244px; top: 161px;
    font: 600 11px/1 "Barlow Semi Condensed", sans-serif; color: var(--ink);
  }
  .side-label {
    position: absolute; top: 607px; width: 80px; text-align: center;
    font: 600 9px/1 "Barlow Semi Condensed", sans-serif; color: var(--ink);
  }
  .side-label--front { left: 359px; }
  .side-label--back { left: 735px; }

  .card {
    position: absolute; top: 255px; width: 203px; height: 345px;
    border: 1px solid var(--card-edge); background: var(--sheet);
  }
  .card--front { left: 298px; }
  .card--back { left: 674px; }

  /* Front */
  .brand-mark {
    position: absolute; left: 83px; top: 32px; width: 36px; height: 36px;
    border-radius: 50%; background: var(--teal);
  }
  .brand-name {
    position: absolute; left: 0; top: 82px; width: 100%; text-align: center;
    font: 500 17px/1 "Source Sans 3", sans-serif; color: var(--brand-blue);
  }
  .brand-tagline {
    position: absolute; left: 0; top: 100px; width: 100%; text-align: center;
    font: 400 4.6px/1 "Source Sans 3", sans-serif; letter-spacing: 1.9px; color: var(--teal);
  }
  .person { position: absolute; left: 0; top: 166px; width: 100%; text-align: center; color: var(--ink); }
  .person-name { font: 400 16px/1.1 "Questrial", sans-serif; margin-bottom: 2px; }
  .person-role { font: 400 9.5px/11.5px "Questrial", sans-serif; }
  .contact { position: absolute; left: 38px; top: 284px; font: 400 10px/12.5px "Questrial", sans-serif; color: var(--ink); }
  .contact-key { font-weight: 700; display: inline-block; width: 12px; }

  /* Back */
  .appointments {
    position: absolute; left: 13px; top: 14px; width: 137px;
    border-collapse: collapse; table-layout: fixed;
  }
  .appointments th, .appointments td {
    border: 1px solid var(--table-line); height: 21px; width: 50%;
  }
  .appointments th {
    font: 400 10px/1 "Source Sans 3", sans-serif; color: var(--brand-blue); text-align: center;
  }
  .spine { position: absolute; left: 148px; top: 14px; width: 40px; height: 316px; }
  .spine-brand {
    position: absolute; left: 160px; top: 26px; writing-mode: vertical-rl;
  }
  .spine-brand-name { font: 500 15.5px/17px "Source Sans 3", sans-serif; color: var(--brand-blue); }
  .spine-brand-tagline { font: 400 4.6px/7px "Source Sans 3", sans-serif; letter-spacing: 1.9px; color: var(--teal); }
  .spine-label {
    position: absolute; left: 163px; top: 204px; writing-mode: vertical-rl;
    font: 400 9.5px/1 "Source Sans 3", sans-serif; letter-spacing: 2.6px; color: var(--on-teal);
  }
</style>
</head>
<body>
<main class="sheet">
  <h1 class="sheet-title">DOUBLE-SIDED BUSINESS CARD DESIGN</h1>
  <div class="sheet-rule"></div>
  <p class="sheet-size">Size: 50mm (W) x 85mm (H)</p>

  <section class="card card--front" aria-label="Card front">
    <div class="brand-mark"></div>
    <p class="brand-name">Summit Wellpath</p>
    <p class="brand-tagline">ACUPUNCTURE PHYSIOTHERAPY</p>
    <div class="person">
      <p class="person-name">Marcus Thelwick</p>
      <p class="person-role">Acupuncturist</p>
      <p class="person-role">Member KPTG</p>
      <p class="person-role">BVF Treatment Provider</p>
    </div>
    <div class="contact">
      <p><span class="contact-key">m</span>: 482 1358 027 514 3820</p>
      <p><span class="contact-key">e</span>: marcus@swpath.example.nz</p>
    </div>
  </section>
  <p class="side-label side-label--front">FRONT</p>

  <section class="card card--back" aria-label="Card back">
    <table class="appointments">
      <thead><tr><th>Time</th><th>Date</th></tr></thead>
      <tbody>
        <tr><td></td><td></td></tr><tr><td></td><td></td></tr><tr><td></td><td></td></tr>
        <tr><td></td><td></td></tr><tr><td></td><td></td></tr><tr><td></td><td></td></tr>
        <tr><td></td><td></td></tr><tr><td></td><td></td></tr><tr><td></td><td></td></tr>
        <tr><td></td><td></td></tr><tr><td></td><td></td></tr><tr><td></td><td></td></tr>
        <tr><td></td><td></td></tr><tr><td></td><td></td></tr>
      </tbody>
    </table>
    <svg class="spine" viewBox="0 0 40 316" aria-hidden="true">
      <path fill="var(--teal)" d="M1,0 H4 Q8,0 8,5 V158 Q8,170 22,174 Q36,178 36,190 V310 Q36,316 30,316 H1 Z"/>
    </svg>
    <div class="spine-brand">
      <p class="spine-brand-name">Summit Wellpath</p>
      <p class="spine-brand-tagline">ACUPUNCTURE PHYSIOTHERAPY</p>
    </div>
    <p class="spine-label">Appointments</p>
  </section>
  <p class="side-label side-label--back">BACK</p>
</main>
</body>
</html>
```